Beauty Salon Design

The business card design will be for a new beauty salon opening up.

The therapist has over 11 years at a leading beauty Salon in perth.

The two colours that the salon will use is black and gold.

Industry/Entity Type

Beauty Salon

Contact Information for Business Card

Lumora Beauty

Corinne Halstead Pryce
Advanced beauty therapist
0455 817 302

Monday - Friday 9am - 2.30pm
Weekends and nights by appointment only

Waxing, Tinting, Swedish massage, hot stone massage, facials, peels, micro, LED light treatment, skin needling and retail products.

```html
<!DOCTYPE html>
<html lang="en">
<head>
<meta charset="utf-8">
<title>Lumora Beauty – Business Card</title>
<link rel="stylesheet" href="https://fonts.googleapis.com/css2?family=Crimson+Text:wght@400;600&family=Libre+Baskerville:wght@700&display=swap">
<style>
  :root {
    --card-black: #231f20;
    --gold: #b8af0a;
    --gold-deep: #8f8806;
    --silver: #9a9a9a;
    --white: #ffffff;
    --page: #ecebe7;
    --skin-light: #b88a6e;
    --skin-dark: #3a2a24;
  }
  * { margin: 0; padding: 0; box-sizing: border-box; }
  html, body { width: 1200px; height: 900px; overflow: hidden; }
  body {
    background: var(--page);
    position: relative;
    font-family: "Crimson Text", Georgia, serif;
  }
  .card {
    position: absolute;
    left: 285px;
    width: 630px;
    height: 360px;
    background: var(--card-black);
    overflow: hidden;
    box-shadow: 0 6px 18px rgba(0,0,0,0.18);
  }
  .card--back { top: 50px; }
  .card--front { top: 490px; }

  /* Back side */
  .back-waves { position: absolute; inset: 0; }
  .back-brand {
    position: absolute; right: 22px; top: 14px;
    font-family: "Libre Baskerville", Georgia, serif;
    font-weight: 700; font-size: 30px; color: var(--gold);
  }
  .back-hours {
    position: absolute; right: 22px; top: 58px; text-align: right;
    font-family: "Libre Baskerville", Georgia, serif; font-weight: 700;
    color: var(--white);
  }
  .back-hours .days { font-size: 21px; }
  .back-hours .note { font-size: 14px; margin-top: 2px; }
  .services {
    position: absolute; list-style: none;
    font-family: "Libre Baskerville", Georgia, serif; font-weight: 700;
    font-size: 14px; line-height: 22px; color: var(--card-black);
  }
  .services li::before { content: "\2605\00a0"; font-size: 11px; }
  .services--main { left: 20px; top: 150px; }
  .services--extra { left: 250px; top: 282px; }

  /* Front side */
  .portrait {
    position: absolute; left: 0; top: 0; width: 400px; height: 360px;
    background:
      linear-gradient(90deg, rgba(35,31,32,0) 55%, var(--card-black) 100%),
      radial-gradient(ellipse at 62% 55%, var(--skin-light) 0%, #7a5646 38%, var(--skin-dark) 70%, var(--card-black) 100%);
  }
  .holder {
    position: absolute; left: 28px; top: 222px; color: var(--white);
  }
  .holder .name { font-size: 27px; line-height: 1.1; }
  .holder .role, .holder .phone { font-size: 18px; line-height: 1.25; }
  .front-brand {
    position: absolute; left: 395px; top: 115px;
    font-size: 38px; font-weight: 600; color: var(--gold);
  }
</style>
</head>
<body>

<section class="card card--back" aria-label="Card back">
  <svg class="back-waves" viewBox="0 0 630 360" width="630" height="360" aria-hidden="true">
    <path d="M0,105 C170,70 330,205 630,262 L630,360 L0,360 Z" fill="var(--gold)"/>
    <path d="M150,78 C280,100 390,215 630,248" fill="none" stroke="var(--silver)" stroke-width="16"/>
    <path d="M60,62 C230,60 350,180 600,230" fill="none" stroke="var(--white)" stroke-width="6"/>
    <path d="M0,108 C180,80 340,215 630,266" fill="none" stroke="var(--gold-deep)" stroke-width="5"/>
  </svg>
  <div class="back-brand">Lumora Beauty</div>
  <div class="back-hours">
    <div class="days">Monday - Friday 9am - 2.30pm</div>
    <div class="note">Weekends and nights by appointment only</div>
  </div>
  <ul class="services services--main">
    <li>Waxing</li>
    <li>Tinting</li>
    <li>Swedish massage</li>
    <li>Hot stone massage</li>
    <li>Facials, Peels</li>
  </ul>
  <ul class="services services--extra">
    <li>Micro, LED light treatment</li>
    <li>Skin needling &amp; Retail products</li>
  </ul>
</section>

<section class="card card--front" aria-label="Card front">
  <div class="portrait" role="img" aria-label="Beauty portrait photograph in profile with gold metallic makeup"></div>
  <div class="holder">
    <div class="name">Corinne Halstead Pryce</div>
    <div class="role">Advanced beauty therapist</div>
    <div class="phone">T: 0455 817 302</div>
  </div>
  <div class="front-brand">Lumora Beauty</div>
</section>

</body>
</html>
```